Bref créative
Harbor Floors & More --- Business card
Harbor Floors & More - thousands of types of tiles
Simple
Mei Dalton
4150 Marwood Ave,
Unit 3B, Concord, ON
L4K 5R8
mei.dalton@harborfloorsmore.example
www.harborfloorsmore.example
Introduction : Harbor Floors & More imports and distributes thousands of types of tiles in limestone, marble, slate, granite, porcelan, ceramic, glass and aluminum for homeowners, builders and contractors. Also providing custom-made solid wood kitchen cabinet and vanities.
the logo of Harbor Floors & More
Logo on Black
Logo on White

```html
<!DOCTYPE html>
<html lang="en">
<head>
<meta charset="UTF-8">
<title>Harbor Floors &amp; More — Business Card</title>
<link href="https://fonts.googleapis.com/css2?family=Open+Sans:wght@400;600;700&display=swap" rel="stylesheet">
<style>
  :root {
    --page-bg: #e9e9e9;
    --card-blue: #1ba3de;
    --card-blue-light: #4cc3f0;
    --card-blue-deep: #148ec6;
    --panel-black: #050505;
    --text-white: #ffffff;
    --text-soft: #e4e4e4;
  }
  * { box-sizing: border-box; margin: 0; padding: 0; }
  html, body {
    width: 1200px; height: 900px; overflow: hidden;
    background: var(--page-bg);
    font-family: "Open Sans", Arial, sans-serif;
  }
  .canvas {
    width: 1200px; height: 900px;
    display: flex; align-items: center; justify-content: center;
  }
  .business-card {
    position: relative;
    width: 840px; height: 480px;
    border-radius: 14px;
    background: linear-gradient(180deg, var(--card-blue-light) 0%, var(--card-blue) 55%, var(--card-blue-deep) 100%);
    box-shadow: 0 12px 30px rgba(0,0,0,0.25);
    overflow: hidden;
  }
  .brand-panel {
    position: absolute; left: 34px; top: 30px;
    width: 772px; height: 180px;
    background: var(--panel-black);
    border-radius: 34px 34px 10px 10px;
    display: flex; align-items: center;
    padding-left: 110px;
    gap: 24px;
  }
  .brand-mark {
    flex: 0 0 40px;
    width: 40px; height: 40px;
    background: var(--card-blue-light);
  }
  .brand-name {
    color: var(--text-white);
    font-weight: 600;
    font-size: 38px;
    letter-spacing: 0.5px;
    line-height: 1;
    white-space: nowrap;
  }
  .divider-band {
    position: absolute; left: 34px; top: 224px;
    width: 772px; height: 34px;
    background: var(--panel-black);
    border-radius: 10px 18px 18px 10px;
  }
  .person-name {
    position: absolute; left: 40px; top: 266px;
    color: var(--text-white);
    font-weight: 700;
    font-size: 22px;
    line-height: 28px;
  }
  .contact-panel {
    position: absolute; left: 0; top: 302px;
    width: 840px; height: 178px;
    background: var(--panel-black);
    padding: 16px 0 0 40px;
  }
  .contact-list { list-style: none; }
  .contact-item {
    display: flex; align-items: flex-start; gap: 8px;
    color: var(--text-soft);
    font-size: 15px; line-height: 1.35;
    margin-bottom: 5px;
  }
  .contact-icon {
    flex: 0 0 16px; width: 16px; height: 16px; margin-top: 2px;
  }
</style>
</head>
<body>
<main class="canvas">
  <article class="business-card">
    <header class="brand-panel">
      <span class="brand-mark"></span>
      <span class="brand-name">HARBOR FLOORS &amp; MORE</span>
    </header>
    <div class="divider-band"></div>
    <h1 class="person-name">Mei Dalton</h1>
    <section class="contact-panel">
      <ul class="contact-list">
        <li class="contact-item">
          <svg class="contact-icon" viewBox="0 0 16 16"><circle cx="8" cy="8" r="8" fill="#fff"/><path d="M4 8.5 L8 4.5 L12 8.5 V12 H4 Z" fill="#000"/></svg>
          <span>4150 Marwood Ave, Unit 3B,<br>Concord, ON L4K 5R8</span>
        </li>
        <li class="contact-item">
          <svg class="contact-icon" viewBox="0 0 16 16"><circle cx="8" cy="8" r="8" fill="#fff"/><path d="M5 4 L7 4 L7.6 6.4 L6.5 7.2 Q7.5 9 8.8 9.6 L9.6 8.5 L12 9.1 L12 11 Q8 11.5 5.3 8 Q4.3 6 5 4 Z" fill="#000"/></svg>
          <span>647-555-0142</span>
        </li>
        <li class="contact-item">
          <svg class="contact-icon" viewBox="0 0 16 16"><circle cx="8" cy="8" r="8" fill="#fff"/><rect x="4" y="5" width="8" height="6" fill="#000"/><path d="M4 5 L8 8.5 L12 5" stroke="#fff" stroke-width="0.9" fill="none"/></svg>
          <span>mei.dalton@harborfloorsmore.example</span>
        </li>
        <li class="contact-item">
          <svg class="contact-icon" viewBox="0 0 16 16"><circle cx="8" cy="8" r="8" fill="#fff"/><circle cx="8" cy="8" r="4.5" fill="none" stroke="#000" stroke-width="1.2"/><path d="M3.5 8 H12.5 M8 3.5 V12.5" stroke="#000" stroke-width="1"/></svg>
          <span>www.harborfloorsmore.example</span>
        </li>
      </ul>
    </section>
  </article>
</main>
</body>
</html>
```